Website for Dorian Welsby

Dorian Welsby, an artist, is looking to replace his ClipVerra video (Canvases of Dorian Welsby) with a new website (dwgallery.net) that functions in much the same way as the ClipVerra video, as a slide show, but which makes it much easier to import images and hold them in a library, and to add, subtract, size, rearrange, and choose transitions for a slide show. It should also allow the user to import and manipulate music with a simple interface that allows the user to expand or contract the duration slightly, excerpt and reassemble passages, and make transitions (fade, overlap, etc.) Each slide should be individually editable for screen duration, type of transition, resolution, size, and brightness, however there should be the ability to override the individual settings and create a global setting or apply certain parameters to a subset of slides, perhaps by checking a box or designating subsets by letter group (A,B,C). It would be helpful if the program automatically looked at certain parameters, particularly the brightness of each image, and auto-corrected to make them all the same, if so desired. There should also be a text editor that allows the user to add text to any slide or to create word slides (at an editing level similar to Photoshop text editing). There would also be the ability to add buttons at any point in the slide show that point to different pages in the site (i.e. "Contact Dorian Welsby".), to take email messages and send them to a list of designated email addresses. The site should have the ability to link to other sites.

Industry/Entity Type

Clipverra

Requirements
Must have
• Ease of Use. I'm painter, not a webmaster.
Nice to have
• Elegance

```html
<!DOCTYPE html>
<html lang="en">
<head>
<meta charset="utf-8">
<title>Dorian Welsby: Artist – Full Computer Screen View</title>
<link href="https://fonts.googleapis.com/css2?family=Great+Vibes&family=Rokkitt:wght@400&family=Tinos&display=swap" rel="stylesheet">
<style>
:root{
  --board:#ffffff;
  --screen:#000000;
  --ink:#111111;
  --light:#ffffff;
  --muted:#d8d8d8;
  --rule:#9a9a9a;
  --sunset-orange:#e0581c;
  --sea-blue:#2a9fd6;
  --deep-red:#b5221a;
  --violet:#7a2a8c;
}
*{box-sizing:border-box;margin:0;padding:0}
html,body{width:1200px;height:1000px;overflow:hidden;background:var(--board)}
.board{position:relative;width:1200px;height:1000px;background:var(--board);font-family:"Tinos",serif;color:var(--ink)}
.screen{position:absolute;background:var(--screen);color:var(--light);overflow:hidden}
.screen-gallery{left:0;top:0;width:600px;height:386px}
.screen-caption{left:600px;top:0;width:600px;height:386px}
.screen-comments{left:300px;top:614px;width:600px;height:386px}
.site-title{position:absolute;top:0;font-family:"Great Vibes",cursive;font-size:31px;line-height:40px;white-space:nowrap;color:var(--light)}
.site-nav{position:absolute;top:9px;font-family:"Great Vibes",cursive;font-size:15px;line-height:20px;white-space:nowrap;color:var(--light)}
.site-nav .divider{display:inline-block;width:1px;height:15px;background:var(--light);margin:0 4px;vertical-align:-2px}
.page-scroll{position:absolute;right:2px;top:0;width:5px;height:372px;background:var(--light);border-radius:3px}
.painting{position:absolute}
.painting-main{left:163px;top:69px;width:268px;height:215px;background:linear-gradient(180deg,#e34a1c 0%,#f08a2a 30%,#3ba7d8 55%,#e0571f 75%,#2b8fcf 100%)}
.painting-banner{left:163px;top:39px;width:268px;height:30px;background:linear-gradient(90deg,#2a9fd6,#e0581c 45%,#3bb0dd 70%,#e8892a)}
.thumb-strip{position:absolute;display:flex;align-items:center;gap:7px}
.thumb{width:42px;height:34px;flex:none}
.thumb.active{height:40px}
.arrow{position:absolute;font-size:22px;line-height:22px;color:var(--light);font-family:"Tinos",serif}
.t1{background:linear-gradient(135deg,#e0581c,#2a9fd6)}
.t2{background:linear-gradient(135deg,#2a9fd6,#e8eef4 60%,#1f6fb0)}
.t3{background:linear-gradient(180deg,#c8581c,#e48a3a)}
.t4{background:linear-gradient(180deg,#e06a2a,#3b8fc8)}
.t5{background:linear-gradient(180deg,#d24a1a,#f0a040 50%,#2a6fb0)}
.t6{background:linear-gradient(135deg,#7a2a8c,#e0581c 50%,#2aa07a)}
.t7{background:linear-gradient(180deg,#e0581c,#2a6fb0)}
.caption{position:absolute;font-size:8px;line-height:10px;text-align:center;color:var(--light)}
.comments-title{position:absolute;font-family:"Great Vibes",cursive;font-size:14px;color:var(--light)}
.comment-list{position:absolute;font-size:7px;line-height:14px;color:var(--light)}
.comment-list .rule{height:1px;background:var(--rule);margin:5px 0}
.list-scroll{position:absolute;width:5px;background:var(--light);border-radius:3px}
.form-prompt{position:absolute;font-family:"Great Vibes",cursive;font-size:12px;text-align:center;color:var(--light)}
.form-label{position:absolute;font-size:7px;text-align:center;color:var(--light)}
.field{position:absolute;background:var(--light)}
.submit{position:absolute;background:#e9e9e9;color:#000;font-size:8px;line-height:11px;text-align:center;border:1px solid #888}
.footer{position:absolute;font-size:6px;font-weight:bold;text-align:center;color:var(--light)}
.note{position:absolute;font-family:"Rokkitt",serif;font-size:22px;line-height:29px;color:var(--ink)}
.board-heading{position:absolute;left:300px;top:446px;width:600px;text-align:center;font-family:"Rokkitt",serif;font-size:68px;line-height:86px;color:var(--ink)}
.pointers{position:absolute;left:0;top:0;width:1200px;height:1000px;pointer-events:none}
</style>
</head>
<body>
<div class="board">

  <section class="screen screen-gallery">
    <h1 class="site-title" style="left:93px">Dorian Welsby: Artist</h1>
    <nav class="site-nav" style="left:363px">About the Artist<span class="divider"></span>Contact</nav>
    <div class="painting painting-main" role="img" aria-label="Featured painting: boats on a sea at sunset in orange and blue"></div>
    <div class="thumb-strip" style="left:129px;top:332px">
      <div class="thumb t1" role="img" aria-label="Thumbnail painting"></div>
      <div class="thumb t2 active" role="img" aria-label="Thumbnail painting"></div>
      <div class="thumb t3" role="img" aria-label="Thumbnail painting"></div>
      <div class="thumb t4" role="img" aria-label="Thumbnail painting"></div>
      <div class="thumb t5" role="img" aria-label="Thumbnail painting"></div>
      <div class="thumb t6 active" role="img" aria-label="Thumbnail painting"></div>
      <div class="thumb t7" role="img" aria-label="Thumbnail painting"></div>
    </div>
    <span class="arrow" style="left:124px;top:340px">«</span>
    <span class="arrow" style="left:456px;top:340px">»</span>
    <div class="page-scroll"></div>
  </section>

  <section class="screen screen-caption">
    <h1 class="site-title" style="left:93px">Dorian Welsby: Artist</h1>
    <nav class="site-nav" style="left:363px">About the Artist<span class="divider"></span>Contact</nav>
    <div class="painting painting-banner" role="img" aria-label="Featured painting scrolled above view"></div>
    <div class="thumb-strip" style="left:128px;top:115px">
      <div class="thumb t1" role="img" aria-label="Thumbnail painting"></div>
      <div class="thumb t2 active" role="img" aria-label="Thumbnail painting"></div>
      <div class="thumb t3" role="img" aria-label="Thumbnail painting"></div>
      <div class="thumb t4" role="img" aria-label="Thumbnail painting"></div>
      <div class="thumb t5" role="img" aria-label="Thumbnail painting"></div>
      <div class="thumb t6 active" role="img" aria-label="Thumbnail painting"></div>
      <div class="thumb t7" role="img" aria-label="Thumbnail painting"></div>
    </div>
    <span class="arrow" style="left:124px;top:124px">«</span>
    <span class="arrow" style="left:455px;top:124px">»</span>
    <p class="caption" style="left:120px;top:173px;width:360px">This is a bird! Birds Fly! The ocean is behind you.The sun is yellow. Trees sway in the wind. This is a test of the caption wrap around. I can't wait to see Dorian Welsby's paintings on here.8</p>
    <h2 class="comments-title" style="left:126px;top:213px">Comments</h2>
    <div class="comment-list" style="left:126px;top:233px;width:340px">
      <div>July 2013 03:33:12 PM</div><div>Michael</div><div>asdf</div>
      <div class="rule"></div>
      <div>July 2013 03:27:14 PM</div><div>Michael</div>
    </div>
    <div class="list-scroll" style="left:463px;top:207px;height:106px"></div>
    <p class="form-prompt" style="left:200px;top:322px;width:208px">How do you like it!</p>
    <p class="form-label" style="left:200px;top:347px;width:208px">Your Name:</p>
    <div class="field" style="left:256px;top:358px;width:82px;height:12px"></div>
    <p class="form-label" style="left:200px;top:373px;width:208px">Your Thoughts:</p>
    <div class="page-scroll"></div>
  </section>

  <section class="screen screen-comments">
    <h1 class="site-title" style="left:93px;top:613px;top:0">Dorian Welsby: Artist</h1>
    <nav class="site-nav" style="left:363px">About the Artist<span class="divider"></span>Contact</nav>
    <p class="caption" style="left:120px;top:54px;width:360px">1This is a bird! Birds Fly! The ocean is behind you.The sun is yellow. Trees sway in the wind. This is a test of the caption wrap around. I can't wait to see Dorian Welsby's paintings on here.</p>
    <div class="comment-list" style="left:126px;top:80px;width:340px">
      <div>... -</div><div>new</div>
      <div class="rule"></div>
      <div>July 2013 09:39:41 AM</div><div>fgsdg</div><div>gdsgdg</div>
      <div class="rule"></div>
      <div>July 2013 09:39:30 AM</div><div>sadf</div>
    </div>
    <div class="list-scroll" style="left:463px;top:89px;height:105px"></div>
    <p class="form-prompt" style="left:196px;top:204px;width:208px">How do you like it!</p>
    <p class="form-label" style="left:196px;top:229px;width:208px">Your Name:</p>
    <div class="field" style="left:256px;top:240px;width:82px;height:12px"></div>
    <p class="form-label" style="left:196px;top:254px;width:208px">Your Thoughts:</p>
    <div class="field" style="left:161px;top:265px;width:275px;height:65px"></div>
    <div class="submit" style="left:283px;top:335px;width:28px;height:12px">Submit</div>
    <p class="footer" style="left:196px;top:361px;width:208px">© Dorian Welsby 2013</p>
    <div class="page-scroll" style="height:386px"></div>
  </section>

  <p class="note" style="left:130px;top:403px">Thumbs (Show as many as you want)</p>
  <p class="note" style="left:655px;top:400px;width:420px">Title and navigation always at top of screen for easy page changing</p>
  <p class="note" style="left:36px;top:458px;width:250px">Image automatically centers vertically and horizontally</p>
  <p class="board-heading">Full Computer Screen View</p>
  <p class="note" style="left:1036px;top:491px;width:150px">Captions (height auto-matically adjusts)</p>
  <p class="note" style="left:130px;top:730px">Comments</p>
  <p class="note" style="left:78px;top:884px;width:200px">Add Comments from Visitors</p>

  <svg class="pointers" viewBox="0 0 1200 1000" aria-hidden="true">
    <g stroke="#ffffff" stroke-width="1.2" fill="none">
      <line x1="180" y1="152" x2="88" y2="386"/>
      <line x1="196" y1="365" x2="183" y2="386"/>
      <line x1="707" y1="48" x2="672" y2="386"/>
      <line x1="1035" y1="190" x2="1082" y2="386"/>
      <line x1="600" y1="282" x2="1060" y2="282"/>
      <line x1="300" y1="768" x2="405" y2="793"/>
      <line x1="300" y1="772" x2="405" y2="796"/>
      <line x1="300" y1="893" x2="461" y2="909"/>
      <line x1="300" y1="897" x2="461" y2="912"/>
    </g>
    <g stroke="#111111" stroke-width="1.2" fill="none">
      <line x1="88" y1="386" x2="84" y2="396"/>
      <line x1="183" y1="386" x2="178" y2="396"/>
      <line x1="672" y1="386" x2="671" y2="396"/>
      <line x1="1082" y1="386" x2="1086" y2="396"/>
      <line x1="222" y1="745" x2="300" y2="768"/>
      <line x1="222" y1="749" x2="300" y2="772"/>
      <line x1="250" y1="888" x2="300" y2="893"/>
      <line x1="250" y1="892" x2="300" y2="897"/>
    </g>
  </svg>
</div>
</body>
</html>
```